Simple elegant business card

General card for a fin and television director.
Just want name, email, phone and address.

Target Market(s)

Prospective employers

Industry/Entity Type

Business

Requirements
Must have
• As above
Nice to have
• Logo but not necessary.
Should not have
• Not too colourful or funky.
• Simplicity and elegance the way to go.

```html
<!DOCTYPE html>
<html lang="en">
<head>
<meta charset="utf-8">
<title>Nora Hale – Business Card</title>
<link href="https://fonts.googleapis.com/css2?family=Arimo:wght@400;700&display=swap" rel="stylesheet">
<style>
  :root {
    --paper: #f6f6f6;
    --ink: #111111;
    --accent: #9b0000;
    --tone-dark: #1c1c1c;
    --tone-red: #8f0a0a;
  }
  html, body {
    margin: 0;
    padding: 0;
    overflow: hidden;
    background: var(--paper);
  }
  .card {
    position: relative;
    width: 1200px;
    height: 686px;
    background: var(--paper);
    overflow: hidden;
    font-family: "Arimo", Arial, sans-serif;
    color: var(--ink);
  }
  .film-artwork {
    position: absolute;
    left: 0;
    top: 0;
    width: 740px;
    height: 686px;
    background: linear-gradient(160deg, var(--tone-dark) 0%, #4a1010 45%, var(--tone-red) 100%);
  }
  .contact {
    position: absolute;
    left: 771px;
    top: 280px;
    padding-left: 25px;
    border-left: 5px solid var(--accent);
  }
  .contact__name {
    margin: -6px 0 0;
    font-size: 58px;
    font-weight: 400;
    line-height: 1;
    letter-spacing: -0.5px;
  }
  .contact__surname {
    font-weight: 700;
    color: var(--accent);
  }
  .contact__line {
    margin: 2px 0 0;
    font-size: 33px;
    line-height: 1.05;
  }
</style>
</head>
<body>
  <main class="card">
    <div class="film-artwork" role="img" aria-label="Illustration of a curving cinema film strip in black and deep red with white frames and sprocket holes"></div>

    <section class="contact">
      <h1 class="contact__name">Nora <span class="contact__surname">Hale</span></h1>
      <p class="contact__line">norahale@mail.com</p>
      <p class="contact__line">+1 310 555 0142</p>
    </section>
  </main>
</body>
</html>
```